Veltrano - Mechanic/Collision Center Business Card

We're looking for a business card design for our mechanic/ collision repair shop.

Can be with colours or monochromatic.

See the attached files.

Many thanks

```html
<!DOCTYPE html>
<html lang="en">
<head>
<meta charset="utf-8">
<title>Veltrano Business Card</title>
<link href="https://fonts.googleapis.com/css2?family=Open+Sans:wght@400;700;800&display=swap" rel="stylesheet">
<style>
  :root {
    --page: #e9e9eb;
    --card-dark: #262628;
    --card-dark-mark: #1a1a1b;
    --card-white: #ffffff;
    --ink: #2b2b2d;
    --ink-soft: #4a4a4d;
    --blue: #1f93d8;
    --band: #2a2a2c;
  }
  * { box-sizing: border-box; margin: 0; padding: 0; }
  html, body {
    width: 1200px; height: 900px; overflow: hidden;
    background: var(--page);
    font-family: "Open Sans", Arial, sans-serif;
  }
  .card {
    position: absolute; left: 250px;
    width: 700px; height: 400px;
    box-shadow: 0 6px 20px rgba(0,0,0,0.18);
    overflow: hidden;
  }
  .card--front { top: 35px; background: var(--card-dark); }
  .card--back { top: 465px; background: var(--card-white); }

  .front-mark {
    position: absolute; left: 0; right: 0; top: 160px;
    text-align: center;
    font-weight: 800; font-size: 64px; letter-spacing: 2px;
    color: var(--card-dark-mark);
  }

  .wave { position: absolute; left: 0; top: 0; width: 700px; height: 400px; }

  .brand {
    position: absolute; left: 50px; top: 175px;
    display: flex; align-items: center; gap: 12px;
  }
  .brand__dot { width: 26px; height: 26px; border-radius: 50%; background: var(--blue); }
  .brand__name {
    font-weight: 800; font-size: 46px; color: var(--ink); letter-spacing: 1px;
  }

  .contact {
    position: absolute; left: 390px; top: 55px;
    border-left: 2px solid var(--blue);
    padding-left: 16px;
    color: var(--ink-soft);
    font-size: 16px; line-height: 1.45;
  }
  .contact__name { color: var(--blue); font-weight: 700; font-size: 24px; line-height: 1.1; }
  .contact__role { margin-bottom: 8px; }
  .contact__address { margin-bottom: 8px; }
  .contact__line { display: flex; align-items: center; gap: 7px; }
  .contact__line svg { width: 13px; height: 13px; fill: var(--blue); flex: none; }

  .website {
    position: absolute; left: 500px; top: 340px;
    transform: rotate(-18deg); transform-origin: left center;
    color: #fff; font-size: 17px; white-space: nowrap;
  }
  .website span { color: var(--blue); }
</style>
</head>
<body>
  <section class="card card--front">
    <div class="front-mark">VELTRANO</div>
  </section>

  <section class="card card--back">
    <svg class="wave" viewBox="0 0 700 400" aria-hidden="true">
      <path d="M0,378 C280,378 480,310 700,238 L700,400 L0,400 Z" fill="var(--band)"/>
      <path d="M150,362 C380,348 540,292 700,216" fill="none" stroke="var(--blue)" stroke-width="9"/>
    </svg>

    <div class="brand">
      <span class="brand__dot"></span>
      <span class="brand__name">VELTRANO</span>
    </div>

    <div class="contact">
      <div class="contact__name">DAN FERRIS</div>
      <div class="contact__role">President</div>
      <div class="contact__address">1820 Harbor Crest Drive<br>Seabrook CA 90412</div>
      <div class="contact__line">
        <svg viewBox="0 0 24 24"><path d="M6.6 10.8a15.1 15.1 0 0 0 6.6 6.6l2.2-2.2c.3-.3.7-.4 1-.2 1.1.4 2.3.6 3.6.6.6 0 1 .4 1 1V20c0 .6-.4 1-1 1C10.6 21 3 13.4 3 4c0-.6.4-1 1-1h3.5c.6 0 1 .4 1 1 0 1.3.2 2.5.6 3.6.1.3 0 .7-.2 1z"/></svg>
        <span>555-240-6180</span>
      </div>
      <div class="contact__line">
        <svg viewBox="0 0 24 24"><path d="M2 5h20v14H2z M2 5l10 8 10-8" stroke="#fff" stroke-width="1.5"/></svg>
        <span>info@veltrano.com</span>
      </div>
    </div>

    <div class="website">www.<span>veltrano</span>.com</div>
  </section>
</body>
</html>
```